BRACKENRIDGE BUILDERS B-Card

I currently have a b-card design but will be removing the image (tree) from the logo and have text only.
I want the card to be classy and strong within the building and construction industry.
I will be using Spot UV on the cards as per the attached examples. I will also send through some sketched ideas that I have in mind.
The color blue is similar to the image (No. 6) attached images

Target Market(s)

middle to maturre aged.
Home Owners / Renovators and Builders

Industry/Entity Type

Construction

Contact Information for Business Card

BRACKENRIDGE BUILDERS
Name: Dermot Quaile
Title: Project Manager
Mobile: 0412 537 804
Office: (08) 9173 5842
Address: 17C Pellworth Avenue, Carrowmere WA 6088
Email: info@brackenridgebuild.com.au
PO Box: 3817 Carrowmere WA 6951

Colors
0592cd
33a6d7
85cae6
1b1b1b

Requirements
Must have
• 1. It must have spot UV on the front of card, maybe back of card too
• 2. I really like the blue on image 6. (or at least a really cool electric blue against the charcoal grey background)
• 3. The font must be slimline and modern. Easy to read
• 4. There must be no black used on the card... Only greys and dark charcoal greys
• 5. Use only the text from the logo "Brackenridge Builders" Not the image of the tree. I am wanting the b-cards to be more masculine.
Nice to have
• 1. I like the design concept on image 6. but happy to see what else you can do with the Spot UV
• 2. Unless you have a really cool idea of the image of the tree (from previous logo) Spot UV somewhere in the design concept thats original and different then I am keen to see what you come up with
• 3. Try changing the color of the logo eg. full white or Blue and white
• 4. Another option is to have the Brackenridge Logo on the front of card with the spot UV in the background of text which we specialise in eg, Roofing, Ceiling, Insulation, Gutter Guards, Electrical, Insurance etc and we can add or reduce items as required. Similar to image 12.
Should not have
• Do not include the image of the tree from previous logo. unless you have a really cool idea of Spot UV somewhere in the design concept thats original and different.

```html
<!DOCTYPE html>
<html lang="en">
<head>
<meta charset="UTF-8">
<title>Brackenridge Builders – Business Card</title>
<link rel="stylesheet" href="https://fonts.googleapis.com/css2?family=Open+Sans:wght@300;400;600;700&display=swap">
<style>
  :root {
    --blue: #0592cd;
    --blue-mid: #33a6d7;
    --blue-light: #85cae6;
    --charcoal: #1b1b1b;
    --card: #1e1e1f;
    --grey-text: #a9a9ab;
    --sub-grey: #bdbdbf;
    --white-text: #ececec;
    --backdrop: #3b3633;
  }
  * { box-sizing: border-box; margin: 0; padding: 0; }
  html, body {
    width: 1200px; height: 864px; overflow: hidden;
    background: var(--backdrop);
    font-family: "Open Sans", Arial, sans-serif;
  }
  .stage {
    position: relative; width: 1200px; height: 864px;
    display: flex; align-items: center; justify-content: center; gap: 40px;
  }
  .card {
    position: relative; width: 540px; height: 330px;
    background: var(--card);
    border-radius: 3px;
    box-shadow: 0 14px 30px rgba(0,0,0,.45);
  }
  .wordmark { text-align: center; line-height: 1; }
  .wordmark .line-main {
    display: block; font-weight: 700; color: var(--blue-mid);
    font-size: 46px; letter-spacing: -0.5px;
  }
  .wordmark .line-sub {
    display: block; font-weight: 400; color: var(--sub-grey);
    font-size: 19px; letter-spacing: 27px; margin-top: 6px; padding-left: 27px;
  }

  /* Back of card */
  .card-back .wordmark { position: absolute; left: 0; right: 0; top: 92px; }
  .card-back .services {
    position: absolute; left: 0; right: 0; top: 210px;
    text-align: center; color: var(--grey-text);
    font-size: 13px; line-height: 1.5;
  }

  /* Front of card */
  .card-front .wordmark { position: absolute; right: 30px; top: 54px; width: 360px; }
  .card-front .wordmark .line-main { font-size: 38px; }
  .card-front .wordmark .line-sub { font-size: 16px; letter-spacing: 22px; padding-left: 22px; margin-top: 5px; }
  .person {
    position: absolute; right: 300px; top: 190px; text-align: right;
  }
  .person .name { color: var(--blue-mid); font-size: 18px; font-weight: 600; }
  .person .role { color: var(--white-text); font-size: 14px; margin-top: 4px; }
  .divider {
    position: absolute; left: 258px; top: 186px; width: 1px; height: 108px;
    background: linear-gradient(var(--grey-text), rgba(169,169,171,0));
  }
  .contact {
    position: absolute; left: 278px; top: 186px;
    color: var(--white-text); font-size: 13px; line-height: 1.45;
    list-style: none;
  }
  .contact li { display: flex; align-items: center; gap: 7px; white-space: nowrap; }
  .contact svg { width: 13px; height: 13px; fill: var(--blue-mid); flex: none; }
</style>
</head>
<body>
<main class="stage">
  <section class="card card-back" aria-label="Business card back">
    <div class="wordmark">
      <span class="line-main">BRACKENRIDGE</span>
      <span class="line-sub">BUILDERS</span>
    </div>
    <p class="services">Roofing | Ceiling | Insulation<br>Gutter Guards | Electrical | Insurance etc</p>
  </section>

  <section class="card card-front" aria-label="Business card front">
    <div class="wordmark">
      <span class="line-main">BRACKENRIDGE</span>
      <span class="line-sub">BUILDERS</span>
    </div>
    <div class="person">
      <p class="name">Dermot Quaile</p>
      <p class="role">Project Manager</p>
    </div>
    <div class="divider"></div>
    <ul class="contact">
      <li>17C Pellworth Avenue</li>
      <li>Carrowmere WA 6088</li>
      <li>PO Box: 3817 Carrowmere WA 6951</li>
      <li><svg viewBox="0 0 16 16" aria-hidden="true"><path d="M3 1h3l1.5 4-2 1.3a9 9 0 0 0 4.2 4.2L11 8.5l4 1.5v3a2 2 0 0 1-2 2A12 12 0 0 1 1 3a2 2 0 0 1 2-2z"/></svg>(08) 9173 5842</li>
      <li><svg viewBox="0 0 16 16" aria-hidden="true"><path d="M4 0h8a1 1 0 0 1 1 1v14a1 1 0 0 1-1 1H4a1 1 0 0 1-1-1V1a1 1 0 0 1 1-1zm1 2v10h6V2zm3 11a1 1 0 1 0 0 2 1 1 0 0 0 0-2z"/></svg>0412 537 804</li>
      <li><svg viewBox="0 0 16 16" aria-hidden="true"><path d="M1 3h14v10H1zm1 1.2V12h12V4.2L8 9z"/></svg>info@brackenridgebuild.com.au</li>
    </ul>
  </section>
</main>
</body>
</html>
```